Harbor fairly.com a website to help those harmed by lending institutions

I am looking for a basic one page website that will be used to collect data from people filling out a form.
I will need certain key words to be optimized in order for the page to show up as high as possible in the search engines.

This web page is for people that have been harmed by their. Bank or lending institution due to inappropriate accounting practices or worse purposeful neglect.

Imagery should include an elderly person on the phone in distress because of over due bills.

Images of late notices
Images of threats of foreclosure.

** This site is to help people that are being unfairly treated even though they have made all their payments on time and the bank is commiting gross negligence.***

Some basic notes to start:

The color scheme should be similar to this site:

https://www.plovermark.example/

Here are some basic notes.

There will be more to follow.

There will need to be a collection form that people can link to and share their story.

Have you or someone you loved been hurt by their financial lending institution?

Have they/ you made all your payments on time only to constantly receive late notice penalties and additional accrued interest ?
Has your credit and good name been tarnished because your banks negligent or purposeful mis-handling of your account has caused the credit bureaus to drop your credit score?
Do you spend hours each month calling your bank to have them clear up their accounting mistakes?
Have you received threatening foreclosure notices even though you've made every payment on time ?

Well if so, you are not alone! This practise or gross incompetence is happening to many others just like you.

Your mortgage, student loan out other debt may have been sold to a new company that simply keeps losing the payments and you have to constantly clear you their errors on your time over and over again.

Budget is flexible based on design.

```html
<!DOCTYPE html>
<html lang="en">
<head>
<meta charset="utf-8">
<title>Harbor fairly.com – Help for those harmed by lending institutions</title>
<link rel="stylesheet" href="https://fonts.googleapis.com/css2?family=Poppins:wght@300;400;500;600&display=swap">
<style>
:root{
  --green:#008f6b;
  --green-ring:#0a9570;
  --mint:#a9ddd0;
  --dark:#201f21;
  --hero-dark:#0d0d10;
  --text:#828282;
  --heading:#151515;
  --line:#e1e1e1;
  --white:#ffffff;
}
*{margin:0;padding:0;box-sizing:border-box}
html,body{width:1200px;height:2791px;overflow:hidden;background:var(--white);font-family:'Poppins',sans-serif}
.page{position:relative;width:1200px;height:2791px;overflow:hidden}
.abs{position:absolute}
.brand{font-weight:600;color:var(--green);display:flex;align-items:center;gap:8px;font-size:26px;letter-spacing:-.3px}
.brand i{display:block;width:16px;height:16px;background:var(--green)}
.hero-title{left:640px;top:178px;width:480px;color:var(--white);font-size:34px;font-weight:500;line-height:1.18}
.hero-sub{left:640px;top:316px;width:380px;color:#e8e8e8;font-size:16px;line-height:1.5;font-weight:300}
.btn-outline{display:flex;align-items:center;justify-content:center;border:2px solid var(--white);color:var(--white);font-size:13px;font-weight:500;width:145px;height:41px}
.checklist{left:120px;top:862px;width:440px;list-style:none}
.checklist li{position:relative;padding-left:40px;color:var(--text);font-size:16px;line-height:1.53;margin-bottom:21px;font-weight:300;text-align:justify}
.checklist svg{position:absolute;left:0;top:4px}
.photo{background:linear-gradient(135deg,#d9d2cc,#b8aaa6)}
.band{left:0;top:1443px;width:1200px;height:479px;background:var(--green)}
.frame{left:121px;top:1503px;width:357px;height:357px;border:5px solid var(--white)}
.band-title{left:640px;top:1540px;width:430px;color:var(--white);font-size:24px;font-weight:500;line-height:1.32}
.band-text{left:640px;top:1683px;width:440px;color:#eaf6f2;font-size:11.5px;line-height:1.75}
.contact-title{left:0;top:1996px;width:1200px;text-align:center;font-size:24px;font-weight:500;color:var(--heading)}
.field{border:1px solid var(--line);font-size:11.5px;color:#9a9a9a;padding:0 22px;display:flex;align-items:center}
.field.area{align-items:flex-start;padding-top:14px}
.submit{left:519px;top:2325px;width:160px;height:39px;background:var(--green);color:var(--white);font-size:13px;font-weight:500;display:flex;align-items:center;justify-content:center}
.foot-text{color:#a9a9a9;font-size:11px;line-height:1.75}
.foot-list{list-style:none}
.foot-list li::before{content:"•";margin-right:8px}
.social{width:13px;height:13px;border:1.5px solid #bdbdbd;border-radius:2px}
</style>
</head>
<body>
<div class="page">

  <!-- Hero -->
  <svg class="abs" style="left:0;top:0" width="1200" height="660" viewBox="0 0 1200 660">
    <path d="M0 515 Q600 760 1200 500 V520 Q600 770 0 535 Z" fill="var(--mint)"/>
    <path d="M0 0 H1200 V495 Q600 750 0 505 Z" fill="var(--hero-dark)"/>
  </svg>
  <div class="abs photo" role="img" aria-label="Elderly man on the phone holding his head in distress" style="left:0;top:0;width:640px;height:620px;background:linear-gradient(90deg,#4a423c 0%,#2b2725 55%,rgba(13,13,16,0) 100%);clip-path:path('M0 0 H640 V620 Q300 600 0 505 Z')"></div>
  <div class="abs brand" style="left:118px;top:34px;color:var(--green)"><i></i>Harbor fairly</div>
  <h1 class="abs hero-title">Have been harmed by your Bank or Lending institution</h1>
  <p class="abs hero-sub">due to inappropriate accounting practices or worse purposeful neglect?</p>
  <a class="abs btn-outline" style="left:640px;top:398px">Contact Now!</a>

  <!-- Questions -->
  <ul class="abs checklist">
    <li><svg width="20" height="20" viewBox="0 0 20 20"><circle cx="10" cy="10" r="8.5" fill="none" stroke="#888" stroke-width="1.4"/><path d="M6 10.2l2.8 2.8L14.2 7.5" fill="none" stroke="#888" stroke-width="1.4"/></svg>Have you made all your payments on time only to constantly receive late notice penalties and additional accrued interest?</li>
    <li><svg width="20" height="20" viewBox="0 0 20 20"><circle cx="10" cy="10" r="8.5" fill="none" stroke="#888" stroke-width="1.4"/><path d="M6 10.2l2.8 2.8L14.2 7.5" fill="none" stroke="#888" stroke-width="1.4"/></svg>Has your credit and good name been tarnished because your banks negligent or purposeful mis-handling of your account has caused the credit bureaus to drop your credit score?</li>
    <li><svg width="20" height="20" viewBox="0 0 20 20"><circle cx="10" cy="10" r="8.5" fill="none" stroke="#888" stroke-width="1.4"/><path d="M6 10.2l2.8 2.8L14.2 7.5" fill="none" stroke="#888" stroke-width="1.4"/></svg>Do you spend hours each month calling your bank to have them clear up their accounting mistakes?</li>
    <li><svg width="20" height="20" viewBox="0 0 20 20"><circle cx="10" cy="10" r="8.5" fill="none" stroke="#888" stroke-width="1.4"/><path d="M6 10.2l2.8 2.8L14.2 7.5" fill="none" stroke="#888" stroke-width="1.4"/></svg>Have you received threatening foreclosure notices even though you've made every payment on time?</li>
  </ul>
  <div class="abs" style="left:698px;top:718px;width:484px;height:484px;border-radius:50%;background:var(--green-ring)"></div>
  <div class="abs photo" role="img" aria-label="Elderly man reading a late notice while holding a mug" style="left:722px;top:742px;width:436px;height:436px;border-radius:50%;background:linear-gradient(135deg,#ece9e6,#9b3a4c 75%)"></div>
  <div class="abs photo" role="img" aria-label="Elderly woman worried while talking on the phone" style="left:638px;top:1040px;width:324px;height:324px;border-radius:50%;background:linear-gradient(135deg,#f1efed,#e9c7d3)"></div>

  <!-- Not alone band -->
  <div class="abs band"></div>
  <div class="abs frame"></div>
  <div class="abs photo" role="img" aria-label="Senior couple reviewing paperwork with an advisor" style="left:140px;top:1522px;width:420px;height:320px;background:linear-gradient(120deg,#a6453a 0%,#d8cfc6 45%,#8aa0b8 100%)"></div>
  <h2 class="abs band-title">Well if so, you are not alone! This practise or gross incompetence is happening to many others just like you.</h2>
  <p class="abs band-text">Your mortgage, student loan out other debt may have been sold to a new company that simply keeps losing the payments and you have to constantly clear you their errors on your time over and over again.</p>
  <a class="abs btn-outline" style="left:640px;top:1778px">Contact US</a>

  <!-- Contact form -->
  <h2 class="abs contact-title">Contact Us Today!</h2>
  <div class="abs field" style="left:199px;top:2061px;width:257px;height:41px">Enter your Name</div>
  <div class="abs field" style="left:472px;top:2061px;width:255px;height:41px">Email</div>
  <div class="abs field" style="left:744px;top:2061px;width:257px;height:41px">Phone</div>
  <div class="abs field" style="left:199px;top:2117px;width:393px;height:41px">Loan/Account Type</div>
  <div class="abs field" style="left:608px;top:2117px;width:393px;height:41px">Name of Bank / Lending institution</div>
  <div class="abs field area" style="left:199px;top:2173px;width:802px;height:119px">Message ...</div>
  <a class="abs submit">Submit</a>

  <!-- Footer -->
  <svg class="abs" style="left:0;top:2440px" width="1200" height="351" viewBox="0 0 1200 351">
    <path d="M0 130 Q600 -110 1200 130 V140 Q600 -90 0 150 Z" fill="var(--mint)"/>
    <path d="M0 150 Q600 -80 1200 150 V351 H0 Z" fill="var(--dark)"/>
  </svg>
  <div class="abs brand" style="left:0;top:2568px;width:1200px;justify-content:center;font-size:24px"><i style="width:14px;height:14px"></i>Harbor fairly</div>
  <p class="abs foot-text" style="left:119px;top:2625px;width:270px">© Copyright 2019 Harbor Fairly Group,<br>All rights reserved.</p>
  <ul class="abs foot-text foot-list" style="left:441px;top:2625px">
    <li>Constantly charged additional accrued interest</li>
    <li>Constantly receive late notice penalties</li>
    <li>Hurt by financial lending institution</li>
    <li>Banks negligent for your account</li>
  </ul>
  <ul class="abs foot-text foot-list" style="left:763px;top:2625px">
    <li>received threatening foreclosure notices</li>
    <li>Accounting mistakes of Banks</li>
    <li>Miss-handling of your account</li>
  </ul>
  <div class="abs social" style="left:1133px;top:2628px"></div>
  <div class="abs social" style="left:1133px;top:2655px;border-radius:50%"></div>

</div>
</body>
</html>
```